Lip Balm tube design

create label/ product print design for Lip balm tubes
Size of tube
76 mm high
24 mm wide

2.75 x 2" h- this is for the main part of tube, not top cap

Current design has been attached for reference. Would like to stick to something similar but need it to "pop" more and be more readable to user
Designs
Vanilla Mint
Citrus Spice
Coconut Lime
Marshmallow Creme
Satsuma Sugar

Designs must include product information (ingredients) as detailed on examples.
Color palette is color but soft, matte tones

```html
<!DOCTYPE html>
<html lang="en">
<head>
<meta charset="utf-8">
<title>Citrus Spice Lip Balm Label</title>
<link href="https://fonts.googleapis.com/css2?family=Cormorant+Garamond:wght@400;500&family=Allison&family=Mrs+Saint+Delafield&display=swap" rel="stylesheet">
<style>
  :root {
    --stage: #323232;
    --label: #cf8660;
    --band: #ad5832;
    --ink: #b4613b;
    --art-light: #c97d57;
    --art-dark: #bf6e47;
    --white: #ffffff;
  }
  * { margin: 0; padding: 0; box-sizing: border-box; }
  html, body { width: 1200px; height: 1200px; overflow: hidden; background: var(--stage); }
  .canvas { position: relative; width: 1200px; height: 1200px; }
  .label {
    position: absolute; left: 110px; top: 106px; width: 980px; height: 988px;
    background: var(--label); overflow: hidden;
  }
  .label > * { position: absolute; }
  .art {
    background: radial-gradient(circle at 60% 50%, var(--art-dark) 0%, var(--art-light) 55%, var(--label) 80%);
  }
  .art--top { left: 482px; top: 0; width: 498px; height: 378px; border-radius: 0 0 0 60%; }
  .art--bottom { left: 0; top: 602px; width: 462px; height: 386px; border-radius: 0 60% 0 0; }
  .band {
    left: 194px; top: -1px; width: 202px; height: 832px;
    background: var(--band); border-radius: 0 0 101px 101px;
  }
  .product-type {
    left: 210px; top: 114px; width: 169px; height: 59px;
    border-top: 3px solid var(--white); border-bottom: 3px solid var(--white);
    color: var(--white); font-family: "Cormorant Garamond", serif; font-size: 37px;
    font-weight: 500; display: flex; align-items: center; justify-content: center; letter-spacing: 0.5px;
  }
  .rotated { transform: rotate(-90deg); transform-origin: center center; }
  .flavour-name {
    left: 26px; top: 485px; width: 400px; height: 130px;
    color: var(--white); font-family: "Cormorant Garamond", serif; font-size: 116px;
    font-weight: 400; line-height: 130px; text-align: center; letter-spacing: 4px;
  }
  .flavour-rule { left: 347px; top: 550px; width: 2px; height: 196px; background: var(--white); }
  .flavour-accent {
    left: 302px; top: 410px; width: 160px; height: 64px;
    color: var(--white); font-family: "Mrs Saint Delafield", cursive; font-size: 78px;
    line-height: 64px; text-align: center;
  }
  .info {
    left: 434px; top: 530px; width: 636px; height: 205px;
    color: var(--ink); display: flex; flex-direction: column;
  }
  .claims {
    display: flex; justify-content: space-between; padding: 0 6px 0 0;
    font-family: "Allison", cursive; font-size: 54px; line-height: 46px; height: 46px;
  }
  .ingredients {
    margin-top: 10px; font-family: "Cormorant Garamond", serif; font-weight: 500;
    font-size: 14px; line-height: 22.5px; text-align: center; padding: 0 30px;
  }
  .maker {
    margin-top: 18px; display: flex; align-items: center; gap: 16px;
    font-family: "Cormorant Garamond", serif; font-weight: 500; font-size: 12px;
  }
  .social { margin-left: auto; display: flex; gap: 10px; margin-right: 90px; }
  .social span { width: 26px; height: 26px; border-radius: 50%; background: var(--band); display: block; }
</style>
</head>
<body>
<div class="canvas">
  <div class="label">
    <div class="art art--top" role="img" aria-label="Engraved line illustration of orange slices, a whole orange and leaves"></div>
    <div class="art art--bottom" role="img" aria-label="Engraved line illustration of an orange, orange slices and leaves"></div>

    <div class="band"></div>
    <div class="product-type">LIP BALM</div>
    <div class="flavour-name rotated">CITRUS</div>
    <div class="flavour-rule"></div>
    <div class="flavour-accent rotated">spice</div>

    <div class="info rotated">
      <div class="claims"><span>plant based</span><span>vegan</span><span>cruelty free</span></div>
      <p class="ingredients">Olive Fruit Oil (Olea Europaea), Coconut Oil (Cocos Nucifera), Shea Butter (Butyrospermum Parkii), Jojoba Seed Oil (Simmondsia Chinensis), Rosehip Seed Oil (Rosa Canina), Vitamin E (Tocopherol), Sunflower Seed Oil (Helianthus Annuus), Vanilla Aroma, Citrus Aurantium Dulcis (Sweet Orange) Oil, Cinnamomum Zeylanicum (Cinnamon) Oil, S. aromaticum (Clove)</p>
      <div class="maker">
        <span>WWW.TERRABALM.CA</span>
        <span>Made by Terra Balm Co., Maple Ridge, AB T0L 2B0</span>
        <div class="social" aria-label="Social media"><span></span><span></span><span></span></div>
      </div>
    </div>
  </div>
</div>
</body>
</html>
```